Trifold Brochure

This is relatively easy. We already have a trifold made we simply want to update the LOOK to look more like our current website. All content would stay the same the only thing that would change would be the fonts, colors and background images to match the current website.

I have attached a word doc of the old trifold brochure. We would want the content to remain on the same pages of the trifold. Again all you are doing is updating the font, logo, colors and any background images. Please comment with any questions.

This is a 5 day project!

Requirements
Must have
• Logo, colors and fonts to match our current website.
http://www.brimfordpanelworks.com/

```html
<!DOCTYPE html>
<html lang="en">
<head>
<meta charset="utf-8">
<title>Brimford Panelworks Trifold Brochure</title>
<link href="https://fonts.googleapis.com/css2?family=Arimo:ital,wght@0,400;0,700;1,700&display=swap" rel="stylesheet">
<style>
:root{
  --backdrop:#a9a9a9;
  --paper-light:#e3ecd3;
  --paper-pale:#eef4e4;
  --olive:#7f9b5f;
  --olive-dark:#5f7a42;
  --olive-soft:#b9cc9c;
  --ink:#3d4a2e;
  --ink-soft:#56653f;
  --white:#ffffff;
}
*{box-sizing:border-box;margin:0;padding:0}
html,body{width:1200px;height:800px;overflow:hidden}
body{background:var(--backdrop);font-family:"Arimo",Arial,sans-serif;color:var(--ink);position:relative}

.inside-spread{position:absolute;left:30px;top:80px;width:840px;height:640px;display:flex;box-shadow:0 6px 18px rgba(0,0,0,.25)}
.panel{position:relative;width:280px;height:640px;background:var(--paper-light);border-right:1px solid rgba(0,0,0,.08);overflow:hidden}
.panel:last-child{border-right:none}
.panel-top-rule{height:8px;background:var(--olive)}
.panel-upper{padding:14px 16px 0;height:292px;overflow:hidden}
.section-title{font-size:11px;font-weight:700;color:var(--olive-dark);margin:6px 0 5px}
.tick-list{list-style:none;font-size:7.6px;line-height:1.4;color:var(--ink-soft)}
.tick-list li{position:relative;padding-left:12px;margin-bottom:2px}
.tick-list li svg{position:absolute;left:0;top:2px}
.body-small{font-size:7.6px;line-height:1.45;color:var(--ink-soft)}
.numbered-list{font-size:7.2px;line-height:1.45;color:var(--ink-soft);padding-left:14px}
.numbered-list li{margin-bottom:3px}

.intro-band{position:absolute;left:0;top:300px;width:840px;height:64px;padding:12px 16px;font-size:7.8px;line-height:1.45;color:var(--ink);z-index:2;overflow:hidden}
.panel-lower{position:absolute;left:0;bottom:0;width:280px;height:276px;background:var(--olive);padding:12px 16px;color:var(--white)}
.photo-row{display:flex;align-items:flex-end;gap:4px;margin-bottom:8px}
.photo{width:120px;height:62px;border:2px solid var(--white)}
.photo.house{background:linear-gradient(180deg,#9bb3c8 0%,#c8cfd2 55%,#6b6a5c 100%)}
.photo.storefront{background:linear-gradient(180deg,#6a5440 0%,#a0805a 50%,#3f3428 100%)}
.photo.drafting{background:linear-gradient(135deg,#f0ebe4 0%,#d9c2b0 60%,#b79a86 100%)}
.icon-box{width:24px;height:24px;background:var(--olive-dark);border:1px solid var(--white);display:flex;align-items:center;justify-content:center}
.square{width:18px;height:18px;background:var(--olive-soft);opacity:.7}
.lower-heading{font-size:11px;font-weight:700;letter-spacing:.3px;text-transform:uppercase;margin-bottom:5px}
.lower-text{font-size:7.2px;line-height:1.45;color:#f1f5ea}
.contact-strip{position:absolute;left:0;bottom:0;width:280px;height:52px;background:var(--olive-soft);padding:8px 14px;display:flex;gap:8px;align-items:center;font-size:6.8px;line-height:1.5;color:var(--ink)}
.contact-strip p{flex:1}
.brand-dot{flex:none;width:10px;height:10px;border-radius:50%;background:var(--olive-dark)}

.cover{position:absolute;left:900px;top:80px;width:270px;height:640px;background:var(--paper-light);box-shadow:0 6px 18px rgba(0,0,0,.25);overflow:hidden}
.cover-logo{height:90px;background:var(--paper-pale);display:flex;align-items:center;justify-content:center;gap:8px;font-weight:700;font-size:16px;color:var(--olive-dark)}
.cover-logo .brand-dot{width:16px;height:16px}
.cover-band{background:var(--olive);padding:12px 18px;color:var(--white);font-weight:700;font-size:21px;line-height:1.15}
.cover-photo{height:250px;background:linear-gradient(180deg,#6b6f86 0%,#b98a74 40%,#e0a66d 52%,#7a6a72 70%,#4d4c5c 100%)}
.cover-slogan{padding:16px 18px 8px;font-size:15px;font-weight:700;font-style:italic;line-height:1.25;color:var(--olive-dark)}
.cover-text{padding:0 18px;font-size:8px;line-height:1.5;color:var(--ink-soft)}
.cover-foot{position:absolute;left:0;bottom:0;width:100%;height:12px;background:var(--olive)}
</style>
</head>
<body>

<div class="inside-spread">
  <section class="panel panel-left">
    <div class="panel-top-rule"></div>
    <div class="panel-upper">
      <h2 class="section-title">Our System includes:</h2>
      <ul class="tick-list">
        <li><svg width="8" height="7" viewBox="0 0 8 7"><path d="M1 4l2 2 4-5" stroke="#5f7a42" stroke-width="1.4" fill="none"/></svg>Collar cut to customer length in sizes ranging from 12" to 144".</li>
        <li><svg width="8" height="7" viewBox="0 0 8 7"><path d="M1 4l2 2 4-5" stroke="#5f7a42" stroke-width="1.4" fill="none"/></svg>Collar Cap with galvanized steel u-bolts to connect to the structure.</li>
        <li><svg width="8" height="7" viewBox="0 0 8 7"><path d="M1 4l2 2 4-5" stroke="#5f7a42" stroke-width="1.4" fill="none"/></svg>Collar spacers to allow for variations in Piling diameter.</li>
        <li><svg width="8" height="7" viewBox="0 0 8 7"><path d="M1 4l2 2 4-5" stroke="#5f7a42" stroke-width="1.4" fill="none"/></svg>Collar Cap spacers to allow for variations in Piling diameter.</li>
        <li><svg width="8" height="7" viewBox="0 0 8 7"><path d="M1 4l2 2 4-5" stroke="#5f7a42" stroke-width="1.4" fill="none"/></svg>Tubes of high strength adhesive glue to connect the Piling to the Collar and for the Collar flange and to fill gaps between the Piling and the Collar, due to the nature of irregular Pilings.</li>
        <li><svg width="8" height="7" viewBox="0 0 8 7"><path d="M1 4l2 2 4-5" stroke="#5f7a42" stroke-width="1.4" fill="none"/></svg>Detailed installation manual providing guidance to the installation contractor.</li>
        <li><svg width="8" height="7" viewBox="0 0 8 7"><path d="M1 4l2 2 4-5" stroke="#5f7a42" stroke-width="1.4" fill="none"/></svg>Detailed written specifications provided in paper format and available in word format upon request.</li>
      </ul>
      <h2 class="section-title">Flexibility:</h2>
      <p class="body-small">Our system has been designed to accommodate piles ranging in diameter from 8" to 12". The system can also correct vertical alignments by up to 6 degrees.</p>
    </div>
    <div class="panel-lower">
      <div class="photo-row">
        <div class="photo house" role="img" aria-label="Photo of a beach house raised on pilings"></div>
        <div class="icon-box"><svg width="14" height="12" viewBox="0 0 14 12"><path d="M1 6L7 1l6 5M3 5v6h8V5" stroke="#fff" stroke-width="1.2" fill="none"/></svg></div>
        <div class="square"></div><div class="square"></div>
      </div>
      <h3 class="lower-heading">Raising a Structure</h3>
      <p class="lower-text">A house on pilings can be raised by disconnecting the house from the pilings, raising the house to create a work area, cutting all of the piles to a preset elevation and installing the Collar on the piling. The Collar is connected with galvanized lag bolts and glued with a high strength adhesive, and gaps are filled with flowable epoxy. The Collar extends above the piling to the bottom of the home's joists. Once set, the concrete provides the compressive strength while the Collar provides tensile and shear strength. A Collar Cap is then installed with two galvanized steel u-bolts which extend into the floor joists.</p>
    </div>
  </section>

  <section class="panel panel-middle">
    <div class="panel-top-rule"></div>
    <div class="panel-lower">
      <div class="photo-row">
        <div class="photo storefront" role="img" aria-label="Photo of a storefront building on repaired pilings"></div>
        <div class="icon-box"><svg width="14" height="12" viewBox="0 0 14 12"><path d="M2 1v10M5 1v10M8 1v10M11 1v10M1 11h12" stroke="#fff" stroke-width="1.2" fill="none"/></svg></div>
        <div class="square"></div><div class="square"></div>
      </div>
      <h3 class="lower-heading">Piling Repairs and Extensions</h3>
      <p class="lower-text">A 36" section of Collar can be installed onto an existing piling and a new section of piling placed on top, with 18" of the Collar covering the top of the existing and 18" covering the bottom of the new piling. Consult with your design professional to ensure the piling length provides the required loading capacity. This connection generally requires lateral support of the pilings.</p>
    </div>
    <div class="contact-strip">
      <span class="brand-dot"></span>
      <p>Brimford Panelworks, LLC - PO Box 4410 - Harlow Ridge, PA 17900-0900<br>T. 555.013.2170 | F. 555.017.0255<br>Email: sales@brimfordpanelworks.com</p>
    </div>
  </section>

  <section class="panel panel-right">
    <div class="panel-top-rule"></div>
    <div class="panel-upper">
      <h2 class="section-title">General Performance Standards, Notes and Guidance:</h2>
      <ol class="numbered-list">
        <li>Vertical load capacity: up to 90 kips in compression.</li>
        <li>Lateral (shear) load capacity: 10 kips.</li>
        <li>Uplift capacity with bolted collar cap: 8 kips.</li>
        <li>All load values are based on independent laboratory testing of installed assemblies and should be confirmed by a licensed engineer for each site.</li>
        <li>Local permitting rules and building codes must be followed for every installation.</li>
        <li>The written installation instructions must be followed. Failure to do so could result in failure of the system.</li>
      </ol>
    </div>
    <div class="panel-lower">
      <div class="photo-row">
        <div class="photo drafting" role="img" aria-label="Photo of hands reviewing construction drawings"></div>
        <div class="icon-box"><svg width="14" height="12" viewBox="0 0 14 12"><path d="M1 11L13 1M1 11h12M4 11L10 5" stroke="#fff" stroke-width="1.2" fill="none"/></svg></div>
        <div class="square"></div><div class="square"></div>
      </div>
      <h3 class="lower-heading">New Construction</h3>
      <p class="lower-text">The standard practice for connecting pilings to floor joists is to notch the pilings and bolt the joists to them. This method weakens the piling and the connection point. Our system uses the Collar, Collar Cap and steel u-bolts as the connection, providing additional strength. A 12" Collar with the cap installed on top of the new piling creates a connection that will outlast the piling by literally thousands of years.</p>
    </div>
  </section>

  <p class="intro-band">Our Patented Piling system has been designed to withstand the corrosive environment of beach communities. The salt water and windblown sand corrodes unprotected materials, and yes, even stainless steel. Our system utilizes a high strength carbon fiber material that is corrosion proof from salt water and UV proof. The system will not erode, decay or loose strength over time. The system has three installation conditions: for raising a house on existing pilings, repairing damaged pilings, and for connecting new pilings to floor joists in new construction. The three options are generally described below.</p>
</div>

<section class="cover">
  <div class="cover-logo"><span class="brand-dot"></span>Brimford Panelworks, LLC</div>
  <div class="cover-band">Build Safer,<br>Build Better</div>
  <div class="cover-photo" role="img" aria-label="Photo of a parent and child holding hands on a beach at sunset"></div>
  <p class="cover-slogan">We provide piling repair systems to allow for cost effective reconstruction and modifications to structures on pilings</p>
  <p class="cover-text">Our system can be installed in a matter of days with a fraction of the typical reconstruction cost. Request our technical brief for a review of how our system compares to other methods.</p>
  <div class="cover-foot"></div>
</section>

</body>
</html>
```